New Company Business Card Design

I have a new company logo and I want a new business card design. I dont know if the logo file i attached is in the correct format or quality. We are a New York City Specialty construction Firm specializing in high risk out of the box projects. I want a simple and classy business card that people will his card is as crisp as the work his company does.

Target Market(s)

Clients in the heavy construction industry in New York City

Industry/Entity Type

Construction Company

Contact Information for Business Card

Simple Classy - DIFFERENT

Font styles to use
Other font styles liked:
• Mach the logo font in some way

Colors

Designer to choose colors to be used in the design.

Requirements
Must have
• Uniqueness
Nice to have
• Nothing particular - Just different and classy - Timeless
Should not have
• Goofy Shit or Gimmicky shit

```html
<!DOCTYPE html>
<html lang="en">
<head>
<meta charset="UTF-8">
<title>KRT Builders, Inc. — Business Cards</title>
<link rel="stylesheet" href="https://fonts.googleapis.com/css2?family=Oswald:wght@500;700&family=Roboto:wght@400;500&display=swap">
<style>
  :root {
    --stage: #c9cacc;
    --charcoal: #32353a;
    --navy: #1f2c3d;
    --concrete: #ececeb;
    --concrete-dark: #dcdcdb;
    --accent: #1e9ae0;
    --white: #ffffff;
    --soft-white: #e4e8ee;
  }
  * { margin: 0; padding: 0; box-sizing: border-box; }
  html, body {
    width: 1200px; height: 1000px; overflow: hidden;
    background: var(--stage);
  }
  .canvas { position: relative; width: 1200px; height: 1000px; }

  .card {
    position: absolute;
    width: 525px; height: 300px;
    overflow: hidden;
    box-shadow: 0 10px 24px rgba(0,0,0,0.18);
  }

  /* Front */
  .card--front {
    left: 90px; top: 130px;
    background: var(--charcoal);
    display: flex; flex-direction: column; align-items: center; justify-content: center;
  }
  .brand {
    display: flex; align-items: center; gap: 10px;
    font-family: "Oswald", sans-serif; font-weight: 700;
    text-transform: uppercase; letter-spacing: 1px;
  }
  .brand__square { width: 14px; height: 14px; }
  .card--front .brand { color: var(--white); font-size: 44px; }
  .card--front .brand__square { background: var(--white); }
  .card--front .website {
    margin-top: 34px;
    font-family: "Roboto", sans-serif; font-size: 15px; font-weight: 500;
    color: var(--accent);
  }

  /* Back */
  .card--back {
    left: 585px; top: 540px;
    background: var(--concrete);
  }
  .back__top {
    position: absolute; left: 0; top: 0; width: 100%; height: 112px;
    background: radial-gradient(circle at 30% 40%, var(--concrete), var(--concrete-dark));
    display: flex; align-items: flex-end; padding: 0 0 16px 26px;
  }
  .card--back .brand { color: var(--accent); font-size: 34px; }
  .card--back .brand__square { background: var(--accent); width: 12px; height: 12px; }

  .back__band {
    position: absolute; left: 0; top: 112px; width: 100%; height: 188px;
    background: var(--navy);
    display: flex; justify-content: space-between;
    padding: 26px 26px 0 26px;
  }
  .person__name {
    font-family: "Oswald", sans-serif; font-weight: 500;
    font-size: 21px; color: var(--accent); line-height: 1.1;
  }
  .person__title {
    font-family: "Roboto", sans-serif; font-size: 13.5px;
    color: var(--soft-white); letter-spacing: 0.3px; margin-top: 3px;
  }
  .contact {
    font-family: "Roboto", sans-serif; font-size: 12.5px;
    color: var(--soft-white); line-height: 1.35;
    list-style: none;
  }
  .contact__address { margin-bottom: 10px; }
  .contact__row { display: flex; align-items: flex-start; gap: 8px; margin-bottom: 4px; }
  .contact__icon { width: 12px; height: 12px; flex: none; margin-top: 2px; }
  .contact__icon svg { display: block; width: 12px; height: 12px; }
</style>
</head>
<body>
<main class="canvas">

  <section class="card card--front" aria-label="Business card front">
    <div class="brand"><span class="brand__square"></span>KRT Builders, Inc.</div>
    <p class="website">www.krtbuilders.com</p>
  </section>

  <section class="card card--back" aria-label="Business card back">
    <div class="back__top">
      <div class="brand"><span class="brand__square"></span>KRT Builders, Inc.</div>
    </div>
    <div class="back__band">
      <div class="person">
        <p class="person__name">Marcus R. Vellano</p>
        <p class="person__title">BUSINESS DEVELOPMENT</p>
      </div>
      <ul class="contact">
        <li class="contact__address">412 Harbor Line Road<br>Linden, New Jersey 07036</li>
        <li class="contact__row">
          <span class="contact__icon"><svg viewBox="0 0 12 12"><path d="M2.5 1 L4.5 1 L5 3.5 L3.8 4.4 Q5 7 7.6 8.2 L8.5 7 L11 7.5 L11 9.5 Q10.5 11 9 11 Q1 10 1 2.5 Q1 1 2.5 1Z" fill="var(--accent)"/></svg></span>
          <span>555-014-2276<br>555-018-3390</span>
        </li>
        <li class="contact__row">
          <span class="contact__icon"><svg viewBox="0 0 12 12"><rect x="0.7" y="2.2" width="10.6" height="7.6" rx="1" fill="none" stroke="var(--accent)" stroke-width="1.2"/><path d="M1 2.8 L6 6.6 L11 2.8" fill="none" stroke="var(--accent)" stroke-width="1.2"/></svg></span>
          <span>MARCUS@krtbuilders.com</span>
        </li>
        <li class="contact__row">
          <span class="contact__icon"><svg viewBox="0 0 12 12"><circle cx="6" cy="6" r="5.3" fill="var(--accent)"/><path d="M0.8 6 H11.2 M6 0.7 Q3 6 6 11.3 M6 0.7 Q9 6 6 11.3" fill="none" stroke="var(--navy)" stroke-width="0.9"/></svg></span>
          <span>www.krtbuilders.com</span>
        </li>
      </ul>
    </div>
  </section>

</main>
</body>
</html>
```